Nonprofit for Addiction Counselors Needs Manual Cover Design

We need a flyer design for a non-profit organization based in Washington, DC called "KELROV, The Guild for Recovery Practitioners". KELROV, the Guild for Recovery Practitioners, represents the professional interests of more than 75,000 addiction counselors, educators and other addiction-focused health care professionals in the United States, Canada and abroad. KELROV’s members are addiction counselors, educators and other addiction-focused health care professionals, who specialize in addiction prevention, treatment, recovery support and education. An important part of the healthcare continuum, KELROV members and its 44 state affiliates work to create healthier individuals, families and communities through prevention, intervention, quality treatment and recovery support.

The purpose of the flyer is to education addiction counselors and other medical professionals about the rules of the Federal Bureau of Transit Safety Regulations for employees with failed drug tests who cannot return to work until they go through addiction treatment and ensure they no longer have a problem. This is the manual that teaches the medical professionals what they need to know to help them get help and get back to work. Here is a link to the product now to learn more about it: http://kelrov-example.org/evaluatorcertificationselfpacedprogram

We would like to see designs that use blue, the main color of our website (www.kelrov-example.org). But are open to other color combinations.

The final design should communicate education and transportation and the United States. Attached is an image of the old cover, which we all dislike a great deal.

Target Market(s)

Our membership potentials are professionals, mostly women and a few men, aged 23 to 65 of all different races who are all trained as therapists and care about people.

Industry/Entity Type

Non-Profit

Requirements
Must have
• The title of the manual is: Recovery Evaluator's F.B.T.S. Impairment and Screening Compliance Certification and Re-certification Program
Must have graphics - if a group of people, must be culturally diverse.
Must contain our logo - three are attached to choose from.
Must be clean and modern/contemporary in tone.
The back cover can just have our logo and our contact information or something else altogether, if you like

```html
<!DOCTYPE html>
<html lang="en">
<head>
<meta charset="utf-8">
<title>KELROV – Recovery Evaluator's F.B.T.S. Program Cover</title>
<link rel="stylesheet" href="https://fonts.googleapis.com/css2?family=Roboto+Condensed:wght@300;700&display=swap">
<style>
  :root {
    --page-bg: #f1f1f1;
    --cover-blue: #0a86cc;
    --cover-blue-light: #1597dc;
    --cover-blue-dark: #0771b0;
    --fold-shade: rgba(0, 0, 0, 0.18);
    --text-white: #ffffff;
    --art-navy: #23317a;
    --art-white: #f4f4f4;
    --art-pink: #eec9cb;
    --art-red: #d9232d;
  }
  * { box-sizing: border-box; margin: 0; padding: 0; }
  html, body {
    width: 1200px;
    height: 1200px;
    overflow: hidden;
    background: var(--page-bg);
    font-family: "Roboto Condensed", "Arial Narrow", sans-serif;
    color: var(--text-white);
  }
  .spread {
    position: absolute;
    left: 40px;
    top: 230px;
    width: 1120px;
    height: 740px;
    display: flex;
    box-shadow: 0 10px 30px rgba(0, 0, 0, 0.15);
  }
  .cover {
    position: relative;
    width: 560px;
    height: 740px;
    background: radial-gradient(ellipse at 50% 45%, var(--cover-blue-light) 0%, var(--cover-blue) 55%, var(--cover-blue-dark) 100%);
  }
  .cover--back { box-shadow: inset -14px 0 18px -12px var(--fold-shade); }
  .cover--front { box-shadow: inset 14px 0 18px -12px var(--fold-shade); }

  .brand {
    position: absolute;
    left: 50%;
    transform: translateX(-50%);
    display: flex;
    flex-direction: column;
    align-items: center;
    gap: 4px;
  }
  .brand__row { display: flex; align-items: center; gap: 8px; }
  .brand__square { width: 26px; height: 26px; background: var(--text-white); }
  .brand__name { font-weight: 700; font-size: 30px; letter-spacing: 0.5px; line-height: 1; }
  .brand__url { font-weight: 300; font-size: 12px; letter-spacing: 0.5px; }
  .cover--back .brand { top: 335px; }
  .cover--front .brand { top: 612px; }

  .title {
    position: absolute;
    top: 76px;
    left: 0;
    width: 100%;
    text-align: center;
  }
  .title__lead { font-weight: 300; font-size: 30px; line-height: 1.15; }
  .title__main { font-weight: 700; font-size: 35px; line-height: 1.2; }
  .title__sub { font-weight: 300; font-size: 22px; line-height: 1.4; margin-top: 2px; }

  .hero-art {
    position: absolute;
    left: 86px;
    top: 274px;
    width: 388px;
    height: 284px;
  }
</style>
</head>
<body>
  <main class="spread">
    <section class="cover cover--back">
      <div class="brand">
        <div class="brand__row">
          <span class="brand__square"></span>
          <span class="brand__name">KELROV</span>
        </div>
        <span class="brand__url">www.kelrov-example.org</span>
      </div>
    </section>

    <section class="cover cover--front">
      <header class="title">
        <p class="title__lead">Recovery Evaluator's</p>
        <h1 class="title__main">F.B.T.S. Impairment and Screening</h1>
        <p class="title__sub">Compliance Certification and Re-certification Program</p>
      </header>

      <svg class="hero-art" viewBox="0 0 388 284" role="img" aria-label="Illustration: map of the United States styled as a flag, with a navy band holding white truck, bus, plane, train and ship icons, and red stripes dripping down over the white map">
        <defs>
          <linearGradient id="heroLower" x1="0" y1="0" x2="0" y2="1">
            <stop offset="0" stop-color="var(--art-white)"/>
            <stop offset="0.55" stop-color="var(--art-pink)"/>
            <stop offset="1" stop-color="var(--art-red)"/>
          </linearGradient>
        </defs>
        <path class="hero-art__band" d="M0 40 Q0 0 40 0 H348 Q388 0 388 40 V96 H0 Z" fill="var(--art-navy)"/>
        <path class="hero-art__field" d="M0 96 H388 V244 Q388 284 348 284 H40 Q0 284 0 244 Z" fill="url(#heroLower)"/>
      </svg>

      <div class="brand">
        <div class="brand__row">
          <span class="brand__square"></span>
          <span class="brand__name">KELROV</span>
        </div>
        <span class="brand__url">www.kelrov-example.org</span>
      </div>
    </section>
  </main>
</body>
</html>
```